Corvale Spine & Joint Business Card

Need a business card using the logo provided. I want brand side of the card to be grey with the logo in the center of the card in white.

On the other side I leave to the designers

Target Market(s)

Personal Injury Attorneys

Industry/Entity Type

Medical

Contact Information for Business Card

Name, CEO. Cell Phone, (Hialeah, Address, Phone) (Homestead, Address, Phone) (Tallahassee, Address, Phone)

Colors

Designer to choose only greyscale colors for use in the design.

Requirements
Must have
• Logo by itself on one side

```html
<!DOCTYPE html>
<html lang="en">
<head>
<meta charset="utf-8">
<title>Corvale Spine &amp; Joint Business Card</title>
<link rel="stylesheet" href="https://fonts.googleapis.com/css2?family=Open+Sans:wght@400;600;700&display=swap">
<style>
  :root {
    --backdrop: #c9c9c9;
    --brand-grey: #ababab;
    --card-white: #ffffff;
    --ink-grey: #a6a6a6;
    --logo-white: #ffffff;
  }
  * { margin: 0; padding: 0; box-sizing: border-box; }
  html, body {
    width: 1200px; height: 1000px; overflow: hidden;
    background: var(--backdrop);
  }
  .stage { position: relative; width: 1200px; height: 1000px; }

  .card { position: absolute; height: 375px; }

  .card-front {
    left: 94px; top: 105px; width: 625px;
    background: var(--brand-grey);
    display: flex; align-items: center; justify-content: center;
  }
  .brand-placeholder {
    color: var(--logo-white);
    font-family: "Open Sans", sans-serif; font-weight: 600;
    font-size: 40px; line-height: 1.2;
    text-align: center;
  }

  .card-back {
    left: 473px; top: 509px; width: 629px;
    background: var(--card-white);
    font-family: "Open Sans", sans-serif;
    color: var(--ink-grey);
  }
  .holder-name {
    position: absolute; left: 46px; top: 101px;
    font-size: 36px; font-weight: 700; line-height: 1.1;
  }
  .holder-title {
    position: absolute; left: 46px; top: 144px;
    font-size: 22px; font-weight: 400; line-height: 1.1;
  }
  .contact-list {
    position: absolute; left: 46px; top: 222px;
    list-style: none;
    display: flex; flex-direction: column; gap: 18px;
  }
  .contact-item {
    display: flex; align-items: center; gap: 14px;
    font-size: 16px; line-height: 26px;
  }
  .contact-item svg { flex: none; display: block; width: 26px; height: 26px; fill: var(--ink-grey); }

  .mini-brand {
    position: absolute; left: 479px; top: 224px;
    width: 119px; height: 119px;
    background: var(--brand-grey);
    display: flex; align-items: center; justify-content: center;
  }
  .mini-brand .brand-placeholder { font-size: 12px; line-height: 1.3; }
</style>
</head>
<body>
<main class="stage">
  <section class="card card-front" aria-label="Card front">
    <div class="brand-placeholder">Corvale Spine &amp; Joint</div>
  </section>

  <section class="card card-back" aria-label="Card back">
    <h1 class="holder-name">Luis Moreno</h1>
    <p class="holder-title">CEO</p>

    <ul class="contact-list">
      <li class="contact-item">
        <svg viewBox="0 0 24 24" aria-label="Phone"><path d="M6.6 2.5c.6-.4 1.4-.3 1.8.3l2.2 3.2c.4.6.3 1.4-.2 1.8L9 9c.9 2.3 3.3 4.9 5.9 6.1l1.3-1.4c.5-.5 1.3-.6 1.8-.2l3.1 2.3c.6.4.7 1.2.3 1.8l-1.3 1.9c-.6.9-1.8 1.3-2.9 1C10.6 19 5.1 13.5 3.6 6.9c-.3-1.1.1-2.2 1-2.9z"/></svg>
        <span>(305) 555-0142</span>
      </li>
      <li class="contact-item">
        <svg viewBox="0 0 24 24" aria-label="Email"><path d="M1.5 5h21v14h-21z M3 6.5v.4l9 6.5 9-6.5v-.4z M3 8.8v8.7h18V8.8l-9 6.4z" fill-rule="evenodd"/></svg>
        <span>luis@corvalespine.com</span>
      </li>
      <li class="contact-item">
        <svg viewBox="0 0 24 24" aria-label="Address"><path d="M12 1.5c-4.2 0-7.5 3.3-7.5 7.4 0 5.3 7.5 13.6 7.5 13.6s7.5-8.3 7.5-13.6c0-4.1-3.3-7.4-7.5-7.4zm0 10.2a2.8 2.8 0 1 1 0-5.6 2.8 2.8 0 0 1 0 5.6z"/></svg>
        <span>120 Palm Ave, Hialeah, FL</span>
      </li>
    </ul>

    <div class="mini-brand">
      <div class="brand-placeholder">Corvale Spine<br>&amp; Joint</div>
    </div>
  </section>
</main>
</body>
</html>
```